Harbor Glow Living.com Landing Page

Create a well designed home/landing page using that communicates the feeling of Harbor Glow Living with this sections that scroll from top to bottom -
Top section - Displays "Harbor Glow Living" with space for embedded YouTube video.

The following sections follow the top section -
Assess your current Harbor Glow Living. Complete our free life balance assessment to identify key areas where you you will most benefit.
"Learn more" call to action button

Create a Harbor Glow Living Study Hub account. Get a 14 day free trial to a wealth of learning activities, motivational videos and professional presentations on our learning portal designed specifically to address the eight essential areas of Harbor Glow Living.
"Register now" call to action button

Get weekly reports on your progress and goal achievement. Celebrate your success each week as you review your progress on each life balance area.

Appropriate royalty free photos and graphics that fit the chosen theme you recommend.
Updates

I'm reviewing the designs. I realize that I need to clarify that Harbor Glow Living focuses on eight areas, not just physical fitness and meditation. Spirituality and Sense of Purpose; Fitness and Health; Relationships; Personal Finance; Recreation and Fun; Physical Environment; Personal Development and Learning; Work and Career

Number of Pages Required

1 page

Colors
33a6d7
00a990
9bcb3c
2f73b3

```html
<!DOCTYPE html>
<html lang="en">
<head>
<meta charset="utf-8">
<title>Harbor Glow Living</title>
<link rel="stylesheet" href="https://fonts.googleapis.com/css2?family=Nunito:wght@400;600;700&family=Lato:wght@400;700&display=swap">
<style>
:root{
  --teal:#55d0bf;
  --teal-soft:#6fd8c6;
  --pink:#ff6584;
  --green:#b1dc57;
  --green-deep:#a5d93b;
  --blue:#4faedc;
  --footer-blue:#33a6d7;
  --slate:#555659;
  --heading:#5f6166;
  --body:#6d6f73;
  --white:#ffffff;
}
*{box-sizing:border-box;margin:0;padding:0}
html,body{width:1200px;height:2365px;overflow:hidden;background:var(--white)}
body{position:relative;font-family:"Lato",sans-serif;color:var(--body)}
.backdrop{position:absolute;left:0;top:0;width:1200px;height:2365px}
.brand{position:absolute;font-family:"Nunito",sans-serif;font-weight:700;font-size:17px;color:var(--white);letter-spacing:.2px}
.nav{position:absolute;top:30px;left:771px;display:flex;gap:0}
.nav a{position:absolute;white-space:nowrap;font-family:"Nunito",sans-serif;font-weight:600;font-size:11.5px;color:#1fb9a4;text-decoration:none}
.nav a.is-active{color:var(--pink)}
.nav a.is-active::after{content:"";position:absolute;left:0;right:0;margin:auto;top:20px;width:14px;height:1.5px;background:var(--pink)}
.hero-title{position:absolute;left:150px;top:158px;font-family:"Nunito",sans-serif;font-weight:400;font-size:35px;line-height:45px;color:var(--white)}
.hero-text{position:absolute;left:150px;top:305px;width:250px;font-size:9.5px;line-height:15px;color:var(--white)}
.btn{position:absolute;width:94px;height:31px;border-radius:16px;font-family:"Nunito",sans-serif;font-weight:700;font-size:8.5px;display:flex;align-items:center;justify-content:center}
.btn-light{background:var(--white);color:#1fb9a4}
.btn-pink{background:var(--pink);color:var(--white)}
.video{position:absolute;left:447px;top:136px;width:602px;height:314px;border-radius:6px;background:linear-gradient(135deg,#6f7b63 0%,#95a57c 45%,#4f5a4b 100%);box-shadow:0 6px 16px rgba(0,0,0,.12);overflow:hidden}
.video svg{position:absolute;left:270px;top:126px}
.art{position:absolute;border-radius:14px}
.section-title{position:absolute;font-family:"Nunito",sans-serif;font-weight:400;font-size:22px;line-height:34px;color:var(--heading)}
.section-text{position:absolute;font-size:9px;line-height:15px;color:var(--body)}
.footer{position:absolute;left:0;top:2183px;width:1200px;height:182px;background:var(--footer-blue);color:var(--white)}
.footer .brand{left:149px;top:34px}
.footer-text{position:absolute;left:149px;top:76px;width:310px;font-size:9.5px;line-height:15px}
.copyright{position:absolute;left:149px;top:131px;font-size:7px}
.footer-col{position:absolute;top:42px;font-family:"Nunito",sans-serif;font-size:9.5px}
.footer-col h4{font-weight:700;font-size:9.5px;margin-bottom:11px}
.footer-col li{list-style:none;margin-bottom:6.5px;line-height:13.5px}
</style>
</head>
<body>
<svg class="backdrop" viewBox="0 0 1200 2365" aria-hidden="true">
  <path fill="var(--teal)" d="M0 0H606C612 50 602 90 590 115C560 180 520 380 505 455C495 510 470 540 420 550C340 560 300 545 240 560C180 575 160 610 130 605C90 600 60 560 0 515Z"/>
  <path fill="var(--pink)" d="M1095 0C1095 50 1140 90 1200 88V0Z"/>
  <path fill="var(--pink)" d="M0 630C30 625 50 650 65 665C80 680 78 720 55 730C35 740 15 735 0 732Z"/>
  <path fill="var(--green)" d="M1200 540C1160 545 1140 580 1110 610C1060 650 1010 670 1012 730C1015 800 1090 850 1200 845Z"/>
  <path fill="var(--blue)" d="M0 1060C40 1040 70 1060 120 1120C180 1190 210 1260 240 1330C255 1390 200 1450 140 1490C90 1520 70 1570 0 1605Z"/>
  <path fill="var(--slate)" d="M1200 1334C1150 1330 1120 1370 1122 1405C1125 1445 1165 1475 1200 1475Z"/>
  <path fill="var(--teal-soft)" d="M1200 1505C1130 1570 1060 1630 960 1670C900 1695 860 1720 830 1750L1070 2080C1110 2040 1160 2010 1200 2010Z"/>
  <path fill="var(--green-deep)" d="M0 2045C60 2015 130 2030 190 2070C250 2110 280 2150 278 2183H0Z"/>
</svg>

<header>
  <div class="brand" style="left:150px;top:28px">Harbor Glow Living</div>
  <nav class="nav">
    <a class="is-active" href="#" style="left:0">Home</a>
    <a href="#" style="left:62px">Services</a>
    <a href="#" style="left:137px">About Us</a>
    <a href="#" style="left:220px">Contact Us</a>
  </nav>
</header>

<section class="hero">
  <h1 class="hero-title">We Help You<br>Find Balance<br>In Life</h1>
  <p class="hero-text">Lorem ipsum dolor sit amet, consetetur sadipscing elitr, sed diam nonumy eirmod tempor invidunt ut labore et dolore magna aliquyam erat, sed diam</p>
  <div class="btn btn-light" style="left:150px;top:375px">Learn More</div>
  <div class="video" role="img" aria-label="Video frame: smiling man in glasses in a green park">
    <svg width="62" height="62" viewBox="0 0 62 62"><circle cx="31" cy="31" r="31" fill="#fff"/><path d="M25 19L43 31L25 43Z" fill="var(--pink)"/></svg>
  </div>
</section>

<section class="assess">
  <h2 class="section-title" style="left:150px;top:791px">Assess your current life balance<br>and wellness</h2>
  <p class="section-text" style="left:150px;top:867px;width:310px">Complete our free life balance assessment to identify key areas where you will most benefit.</p>
  <div class="btn btn-pink" style="left:150px;top:920px">Learn More</div>
  <div class="art" style="left:603px;top:793px;width:445px;height:324px;background:radial-gradient(ellipse at 55% 40%,#c7e58a 0%,#eeeeee 55%,#ffffff 80%)" role="img" aria-label="Illustration: friends standing beside a heart-shaped tree"></div>
</section>

<section class="portal">
  <div class="art" style="left:82px;top:1200px;width:441px;height:355px;background:linear-gradient(135deg,#e9f3f9 0%,#f1f1f1 60%,#cfe6f3 100%)" role="img" aria-label="Illustration: person beside a browser window showing a profile page"></div>
  <h2 class="section-title" style="left:600px;top:1330px">Create a Harbor Glow Living<br>Study Hub account</h2>
  <p class="section-text" style="left:600px;top:1406px;width:405px">Get a 14 day free trial to a wealth of learning activities, motivational videos and professional presentations on our learning portal designed specifically to address the eight essential areas of Harbor Glow Living.</p>
  <div class="btn btn-pink" style="left:600px;top:1474px">Register now</div>
</section>

<section class="reports">
  <h2 class="section-title" style="left:149px;top:1779px">Get weekly reports on your<br>progress and goal achievement.</h2>
  <p class="section-text" style="left:149px;top:1853px;width:315px">Celebrate your success each week as you review your progress on each life balance area.</p>
  <div class="btn btn-pink" style="left:149px;top:1906px">Learn More</div>
  <div class="art" style="left:588px;top:1730px;width:480px;height:375px;background:linear-gradient(135deg,#d9d6f2 0%,#eef3f7 45%,#8fd0ee 100%)" role="img" aria-label="Illustration: man beside a tablet showing progress charts"></div>
</section>

<footer class="footer">
  <div class="brand">Harbor Glow Living</div>
  <p class="footer-text">Lorem ipsum dolor sit amet, consetetur sadipscing elitr, sed diam nonumy eirmod tempor invidunt ut labore et dolore magna aliquyam erat, sed diam voluptua.</p>
  <p class="copyright">Copyright©2020 Harbor Glow Living. All rights Reserved</p>
  <div class="footer-col" style="left:598px"><h4>Explore</h4><ul><li>Features</li><li>Pricing</li><li>Example</li><li>Courses</li></ul></div>
  <div class="footer-col" style="left:787px"><h4>Company</h4><ul><li>About</li><li>Careers</li><li>Blog</li><li>Affiliates</li></ul></div>
  <div class="footer-col" style="left:981px"><h4>Support</h4><ul><li>Knowledge Base</li><li>Contact Support</li><li>Contact Sales</li><li>Privacy Policy</li><li>Terms Of Use</li></ul></div>
</footer>
</body>
</html>
```